Need a fully working bigcommerce fashion apparel website

We are starting a bigcommerce fashion and apparel store. There we need a fully working bigcommerce website. The website themes should be good looking and attract more visitors. Please see the attachment for details.

Coding

Coded - Design and coding required

Font styles to use
Sans Serif

```html
<!DOCTYPE html>
<html lang="en">
<head>
<meta charset="utf-8">
<title>Linen Loom — Independent Fashion Store</title>
<link href="https://fonts.googleapis.com/css2?family=Montserrat:wght@400;500;600;700;800&family=Merriweather+Sans:wght@300;400&display=swap" rel="stylesheet">
<style>
:root{
  --blue:#2f9bf5;
  --navy:#1b2d57;
  --ink:#1d1d1f;
  --muted:#6b6b6b;
  --line:#dedede;
  --band:#e9e9eb;
  --white:#ffffff;
  --topbar:#f4f2f2;
}
*{box-sizing:border-box;margin:0;padding:0}
html,body{width:1200px;height:3818px;overflow:hidden}
body{position:relative;background:var(--white);font-family:"Montserrat",sans-serif;color:var(--ink)}
.abs{position:absolute}
a{color:inherit;text-decoration:none}

/* top bar */
.topbar{left:0;top:0;width:1200px;height:41px;background:var(--topbar);font-size:13px;font-weight:600;color:#222}
.topbar span{position:absolute;top:14px}
/* header */
.header{left:0;top:41px;width:1200px;height:112px}
.logo{position:absolute;left:0;width:1200px;text-align:center;font-weight:600;letter-spacing:10px;color:var(--blue)}
.header .logo{top:30px;font-size:32px}
.util{position:absolute;top:50px;font-size:12px;color:#777;display:flex;align-items:center;gap:8px;letter-spacing:.5px}
/* nav */
.nav{left:0;top:153px;width:1200px;height:51px;border-top:1px solid var(--line);border-bottom:1px solid var(--line)}
.nav a,.fnav a{position:absolute;top:18px;font-size:14px;font-weight:500;transform:translateX(-50%);white-space:nowrap}
.nav a.active{color:var(--blue)}
/* hero */
.hero{left:0;top:204px;width:1200px;height:574px;background:linear-gradient(90deg,#c9b8a2 0%,#b9ab99 45%,#9c9288 70%,#a39a91 100%)}
.hero h1{position:absolute;left:130px;top:150px;font-size:41px;line-height:53px;font-weight:800;color:#fff;letter-spacing:1px}
.btn-blue{position:absolute;background:var(--blue);color:#fff;font-weight:700;text-align:center}
.hero .btn-blue{left:135px;top:288px;width:164px;height:53px;line-height:53px;font-size:19px}
.dots{position:absolute;left:536px;top:523px;display:flex;gap:16px;align-items:center}
.dots i{width:12px;height:12px;border-radius:50%;background:#fff;display:block}
.dots i.on{width:16px;height:16px;background:var(--blue);border:3px solid #fff}
/* section titles */
.stitle{left:0;width:1200px;text-align:center;font-size:26px;font-weight:800;display:flex;justify-content:center;align-items:center;gap:16px}
.stitle::before,.stitle::after{content:"";width:30px;height:3px;background:var(--blue)}
/* category tiles */
.tile{background:#e6e6e8}
.tile .lbl{position:absolute;left:18px;font-size:16px;font-weight:600;line-height:20px}
.tile .sn{position:absolute;left:18px;font-size:11px;font-weight:700;border:1.5px solid #111;padding:3px 6px;background:#fff}
/* products */
.band{left:0;top:1459px;width:1200px;height:645px;background:var(--band)}
.pimg{background:#fff}
.pname{text-align:center;font-size:14px;line-height:17px;width:320px}
.price{text-align:center;width:320px;font-size:24px;font-weight:700;color:var(--blue)}
/* about */
.about-box{left:628px;top:2255px;width:439px;height:355px;border:3px solid var(--blue)}
.about-text{left:736px;top:2292px;width:318px;font-family:"Merriweather Sans",sans-serif;font-size:13.5px;line-height:20px;color:#222;font-weight:300}
.about-text p+p{margin-top:20px}
.readmore{font-size:13px;font-weight:700;color:var(--blue);text-decoration:underline}
/* recent */
.recent{left:130px;top:2793px;width:937px;height:429px;background:var(--blue)}
.recent h3{position:absolute;left:64px;top:50px;width:300px;font-size:27px;line-height:38px;font-weight:700;color:#fff}
.recent p{position:absolute;left:64px;top:180px;width:285px;font-family:"Merriweather Sans",sans-serif;font-size:13.5px;line-height:20px;color:#fff;font-weight:300}
.recent .btn-white{position:absolute;left:64px;top:308px;width:110px;height:29px;line-height:29px;background:#fff;color:var(--blue);font-size:11px;font-weight:700;text-align:center}
/* features */
.feature{top:3283px;width:268px;height:73px;border:1px solid #cfcfcf;display:flex;align-items:center;padding-left:30px;gap:14px}
.feature b{display:block;font-size:13px;font-weight:700;color:#333}
.feature small{display:block;font-size:11px;color:#777;margin-top:4px}
/* footer */
.footer{left:0;top:3400px;width:1200px;height:375px;background:var(--blue);color:#fff}
.footer .logo{top:60px;font-size:32px;color:#fff}
.fnav a{top:166px}
.fcol{position:absolute;text-align:center;font-size:13.5px;font-weight:500;line-height:18px}
.email{position:absolute;left:413px;top:280px;width:372px;height:42px;background:#fff;color:#333;font-size:11px;padding:15px 18px}
.cards{position:absolute;left:847px;top:307px;display:flex;gap:4px}
.cards i{width:28px;height:20px;background:#fff;border-radius:2px;display:block}
.copy{left:0;top:3775px;width:1200px;height:43px;background:var(--navy);color:#fff;font-size:11px;text-align:center;line-height:43px}
</style>
</head>
<body>

<div class="abs topbar">
  <span style="left:130px">FREE SHIPPING ON ORDERS OVER $75</span>
  <span style="right:132px">PHONE: 1300 555 010</span>
</div>

<header class="abs header">
  <div class="util" style="left:134px">
    <svg width="16" height="16" viewBox="0 0 16 16" fill="none" stroke="#333" stroke-width="1.5"><circle cx="8" cy="5" r="3"/><path d="M2 15c0-4 3-5 6-5s6 1 6 5z"/></svg>
    <span style="width:1px;height:24px;background:var(--line);margin:0 10px"></span>
    <svg width="14" height="14" viewBox="0 0 14 14" fill="none" stroke="#333" stroke-width="2"><circle cx="6" cy="6" r="4.5"/><path d="M9.5 9.5L13 13"/></svg>
    <span>SEARCH</span>
  </div>
  <div class="logo">LINEN LOOM</div>
  <div class="util" style="left:878px">WISHLIST
    <svg width="16" height="14" viewBox="0 0 16 14" fill="none" stroke="#444" stroke-width="1.4"><path d="M8 13S1 8.5 1 4.5A3.5 3.5 0 0 1 8 3a3.5 3.5 0 0 1 7 1.5C15 8.5 8 13 8 13z"/></svg>
  </div>
  <div class="util" style="left:990px">
    <svg width="22" height="18" viewBox="0 0 22 18" fill="none" stroke="var(--blue)" stroke-width="1.6"><path d="M1 1h3l3 11h11l3-8H5.5"/><circle cx="8" cy="16" r="1.4"/><circle cx="17" cy="16" r="1.4"/></svg>
    CART (0)
  </div>
</header>

<nav class="abs nav">
  <a class="active" style="left:199px">HOME</a>
  <a style="left:313px">BRANDS</a>
  <a style="left:480px">EXCLUSIVE BRANDS</a>
  <a style="left:684px">PRINT ON DEMAND</a>
  <a style="left:841px">ABOUT US</a>
  <a style="left:976px">CONTACT US</a>
</nav>

<section class="abs hero" role="img" aria-label="Model in a grey checked double-breasted jacket and sunglasses against a blurred wall">
  <h1>CHECKED DOUBLE-<br>BREASTED JACKET</h1>
  <a class="btn-blue">SHOP NOW</a>
  <div class="dots"><i></i><i></i><i class="on"></i><i></i><i></i></div>
</section>

<h2 class="abs stitle" style="top:831px">SHOP BY CATEGORY</h2>

<div class="abs tile" style="left:130px;top:908px;width:266px;height:489px;background:linear-gradient(160deg,#e9e9ea 30%,#9a7a56 70%,#5b4330)" role="img" aria-label="Young man in a brown parka jacket">
  <div class="lbl" style="top:36px">MEN'S<br>FASHION</div><div class="sn" style="top:86px">SHOP NOW</div>
</div>
<div class="abs tile" style="left:404px;top:908px;width:255px;height:240px;background:linear-gradient(90deg,#e4e4e6 45%,#b9b9bb 70%,#dcdcde)" role="img" aria-label="Woman in a zebra print dress">
  <div class="lbl" style="top:36px">WOMEN'S<br>FASHION</div><div class="sn" style="top:86px">SHOP NOW</div>
</div>
<div class="abs tile" style="left:668px;top:908px;width:397px;height:240px;background:linear-gradient(90deg,#e2e2e4 55%,#c9584a 75%,#dddddf)" role="img" aria-label="Red floral wrap skirt with white top">
  <div class="lbl" style="left:45px;top:73px">INDEPENDENT<br>BRANDS</div><div class="sn" style="left:45px;top:123px">SHOP NOW</div>
</div>
<div class="abs tile" style="left:404px;top:1157px;width:398px;height:240px;background:linear-gradient(110deg,#6f8fb0 0%,#b9b3b0 40%,#c86a5e 75%,#a64c44)" role="img" aria-label="Close-up of a silver hand chain bracelet">
  <div class="lbl" style="left:23px;top:48px;color:#fff">MARLOW<br>COLLECTION</div><div class="sn" style="left:23px;top:106px;background:transparent;color:#fff;border-color:#fff">SHOP NOW</div>
</div>
<div class="abs tile" style="left:810px;top:1157px;width:255px;height:240px;background:linear-gradient(90deg,#f2f2f3 42%,#2a2a2a 60%,#1f1f1f 85%,#efefef)" role="img" aria-label="Black slogan swimsuit">
  <div class="lbl" style="top:70px">TESSOR</div><div class="sn" style="top:104px">SHOP NOW</div>
</div>

<div class="abs band"></div>
<h2 class="abs stitle" style="top:1503px">OUR PRODUCTS</h2>
<svg class="abs" style="left:66px;top:1770px" width="20" height="30" viewBox="0 0 20 30" fill="none" stroke="#888" stroke-width="3"><path d="M16 2L4 15l12 13"/></svg>
<svg class="abs" style="left:1094px;top:1770px" width="20" height="30" viewBox="0 0 20 30" fill="none" stroke="#888" stroke-width="3"><path d="M4 2l12 13L4 28"/></svg>

<div class="abs pimg" style="left:136px;top:1638px;width:286px;height:285px;background:linear-gradient(180deg,#fff 10%,#2e8b3a 35%,#1f7a2e)" role="img" aria-label="Man in a green graphic t-shirt"></div>
<div class="abs pname" style="left:119px;top:1943px">#1 Dad Mens Green Funny Fathers Day Graphic Shirt Unique Dad Gifts</div>
<div class="abs price" style="left:119px;top:1994px">$27.00</div>

<div class="abs pimg" style="left:461px;top:1573px;width:286px;height:350px;background:linear-gradient(180deg,#b8b8ba,#3a3a3c 45%,#2a2a2c)" role="img" aria-label="Woman in a black floral summer sundress"></div>
<div class="abs pname" style="left:441px;top:1943px">Women Summer Boho<br>Holiday Sundress</div>
<div class="abs price" style="left:441px;top:1985px">$38.25</div>
<a class="btn-blue abs" style="left:550px;top:2025px;width:106px;height:28px;line-height:28px;font-size:11px">ADD TO CART</a>

<div class="abs pimg" style="left:781px;top:1638px;width:286px;height:285px;background:radial-gradient(circle at 50% 65%,#e8c96a 0,#f5e6b5 18%,#fff 40%)" role="img" aria-label="Gold plated four leaf clover necklace"></div>
<div class="abs pname" style="left:762px;top:1943px">14k Gold Plated Sterling<br>Silver Four Leaf Clover</div>
<div class="abs price" style="left:762px;top:1994px">$65.00</div>

<h2 class="abs stitle" style="top:2159px">ABOUT US</h2>
<div class="abs" style="left:130px;top:2233px;width:580px;height:416px;background:linear-gradient(100deg,#c9ccd6 0%,#e6e6ea 25%,#4a3a3e 45%,#3a2e33 65%,#d6d8de 90%)" role="img" aria-label="Woman in a zebra print wrap dress with a belt"></div>
<div class="abs about-box"></div>
<div class="abs about-text">
  <p>Lorem Ipsum is simply dummy text of the printing and typesetting industry. Lorem Ipsum has been the industry's standard dummy text ever since the 1500s, when an unknown printer took a galley of type and scrambled it to make a type specimen book. It has survived not only five centuries, but also the leap into electronic</p>
  <p>There are many variations of passages of Lorem Ipsum available, but the majority have suffered alteration in some form, by injected humour, or randomised words which don't look even slightly believable. If you are going to use a passage of Lorem Ipsum, you need to be sure there</p>
</div>
<a class="abs readmore" style="left:736px;top:2625px">READ MORE</a>

<h2 class="abs stitle" style="top:2723px">RECENT PRODUCTS</h2>
<div class="abs recent">
  <h3>Sexy Solid Deep-V Swimwear Summer Bathing Suit</h3>
  <p>There are many variations of passages of Lorem Ipsum available, but the majority have suffered alteration in some form, by injected humour, or randomised words which don't look even slightly believable. If</p>
  <a class="btn-white">READ MORE</a>
</div>
<div class="abs" style="left:550px;top:2828px;width:579px;height:353px;background:linear-gradient(90deg,#c9c4c2 0%,#b1aaa7 40%,#8c6a5a 55%,#e9e9e9 65%,#b8b1ae 85%)" role="img" aria-label="Model in a white deep-V belted swimsuit"></div>

<div class="abs feature" style="left:22px">
  <svg width="40" height="28" viewBox="0 0 40 28" fill="none" stroke="#333" stroke-width="1.5"><path d="M8 4h18v16H8zM26 10h7l5 5v5H26"/><circle cx="13" cy="22" r="3" fill="#fff"/><circle cx="32" cy="22" r="3" fill="#fff"/><path d="M1 9h5M3 13h4"/></svg>
  <div><b>Free Ground Shipping</b><small>Inside the United States</small></div>
</div>
<div class="abs feature" style="left:316px">
  <svg width="30" height="28" viewBox="0 0 30 28" fill="none" stroke="#333" stroke-width="1.5"><path d="M4 8h20l-4-4M26 20H6l4 4"/><path d="M4 8a4 4 0 0 0 0 6M26 20a4 4 0 0 0 0-6" stroke="var(--blue)"/></svg>
  <div><b>Free Exchanges</b><small>30 day guarantee on all items</small></div>
</div>
<div class="abs feature" style="left:610px">
  <svg width="34" height="28" viewBox="0 0 34 28" fill="none" stroke="#333" stroke-width="1.5"><rect x="2" y="4" width="24" height="16" rx="2"/><path d="M2 9h24"/><rect x="20" y="16" width="10" height="9" rx="1" stroke="var(--blue)"/></svg>
  <div><b>Safe Payments</b><small>Trusted SSL Protection</small></div>
</div>
<div class="abs feature" style="left:904px">
  <svg width="28" height="28" viewBox="0 0 28 28" fill="none" stroke="#333" stroke-width="1.5"><path d="M14 2l10 4v8c0 6-5 10-10 12C9 24 4 20 4 14V6z"/><path d="M9 14l4 4 7-8" stroke="var(--blue)"/></svg>
  <div><b>Amazing Selection</b><small>We carry all top brands</small></div>
</div>

<footer class="abs footer">
  <div class="logo">LINEN LOOM</div>
  <div class="fnav">
    <a style="left:199px">HOME</a>
    <a style="left:313px">BRANDS</a>
    <a style="left:480px">EXCLUSIVE BRANDS</a>
    <a style="left:684px">PRINT ON DEMAND</a>
    <a style="left:841px">ABOUT US</a>
    <a style="left:976px">CONTACT US</a>
  </div>
  <div class="fcol" style="left:124px;width:200px;top:245px;line-height:38px">SHIPPING AND RETURNS.<br>TERMS &amp; CONDITIONS<br>FAQ</div>
  <div class="fcol" style="left:400px;width:400px;top:245px">SIGN UP FOR THE LATEST NEWS AND OFFERS</div>
  <div class="email">E MAIL ID
    <svg style="position:absolute;right:12px;top:13px" width="18" height="16" viewBox="0 0 18 16" fill="#2a8f8f"><path d="M1 8L17 1 13 15 9 10z"/></svg>
  </div>
  <div class="fcol" style="left:816px;width:280px;top:245px">88 MAPLE ROW AVENUE,<br>WESTBROOK, CA 12345</div>
  <div class="cards"><i></i><i></i><i></i><i></i><i></i><i></i><i></i></div>
</footer>
<div class="abs copy">Copyright © 2020 All Rights Reserved</div>

</body>
</html>
```